SkyvoraQ Business Cards and Stationary Design

Need a design for our business cards and stationary. I want to carry on the theme of the logo. I want the business cards to have a design on the back. I would like the business cards and the stationary to carry the same theme, design scheme, and branding

Target Market(s)

Airlines and Maintenance Facilities

Industry/Entity Type

Aviation

Contact Information for Business Card

Name
Position Title
Address: 4827 Tollbeck Lane, Fort Pierce, Florida, 34951
Office Number
Mobile Number
Email
Website

Font styles to use
Serif
Sans Serif

Colors

Designer to choose colors to be used in the design.

```html
<!DOCTYPE html>
<html lang="en">
<head>
<meta charset="utf-8">
<title>SkyvoraQ Business Card</title>
<link href="https://fonts.googleapis.com/css2?family=Arimo:wght@400;700&display=swap" rel="stylesheet">
<style>
  :root {
    --navy: #15284f;
    --ink: #16244a;
    --sky: #1ea7e0;
    --card: #ffffff;
  }
  html, body { margin: 0; padding: 0; overflow: hidden; }
  body {
    width: 1200px; height: 1200px;
    background: var(--navy);
    position: relative;
    font-family: "Arimo", Arial, sans-serif;
    color: var(--ink);
  }
  .card {
    position: absolute;
    top: 458px;
    width: 522px; height: 314px;
    background: var(--card);
    box-shadow: 6px 8px 14px rgba(0,0,0,0.35);
  }
  .card--front { left: 56px; }
  .card--back { left: 623px; }

  .holder { position: absolute; left: 112px; top: 132px; }
  .holder__name {
    margin: 0; font-size: 21px; font-weight: 700; color: var(--sky);
    line-height: 1; letter-spacing: 0.2px;
  }
  .holder__title { margin: 4px 0 0; font-size: 14.5px; line-height: 1.1; }

  .divider {
    position: absolute; left: 261px; top: 108px;
    width: 2px; height: 97px; background: var(--ink);
  }

  .contact { position: absolute; left: 281px; top: 104px; font-size: 12.4px; line-height: 15.5px; }
  .contact__address { margin: 0 0 6px; }
  .contact__row { display: flex; align-items: center; height: 25.6px; }
  .contact__icon { width: 11px; height: 11px; margin-right: 7px; flex: none; }

  .brand {
    position: absolute; left: 0; right: 0; top: 80px;
    display: flex; flex-direction: column; align-items: center;
  }
  .brand__mark {
    width: 80px; height: 80px; border-radius: 50%;
    border: 4px solid var(--sky); box-sizing: border-box;
  }
  .brand__name {
    margin-top: 16px; font-size: 33px; font-weight: 700;
    letter-spacing: 6px; color: var(--ink); line-height: 1;
  }
  .website {
    position: absolute; left: 0; right: 0; top: 270px; text-align: center;
    font-size: 12.5px; letter-spacing: 8.2px; color: var(--ink);
  }
</style>
</head>
<body>
  <section class="card card--front">
    <div class="holder">
      <h1 class="holder__name">JONH SMITH</h1>
      <p class="holder__title">Position Title</p>
    </div>
    <div class="divider"></div>
    <div class="contact">
      <p class="contact__address">4827 Tollbeck Lane,<br>Fort Pierce, Florida, 34951</p>
      <div class="contact__row">
        <svg class="contact__icon" viewBox="0 0 12 12"><circle cx="6" cy="6" r="5.3" fill="none" stroke="#1ea7e0" stroke-width="1"/><path d="M4 3.5l1 1-.5.8c.4.8 1 1.4 1.8 1.8l.8-.5 1 1-.7.8C5.6 8.2 3.8 6.4 3.6 4.3z" fill="#1ea7e0"/></svg>
        <span>123 456 7890</span>
      </div>
      <div class="contact__row">
        <svg class="contact__icon" viewBox="0 0 12 12"><circle cx="6" cy="6" r="5.3" fill="none" stroke="#1ea7e0" stroke-width="1"/><rect x="3.3" y="4" width="5.4" height="4" fill="none" stroke="#1ea7e0" stroke-width="0.9"/><path d="M3.3 4l2.7 2 2.7-2" fill="none" stroke="#1ea7e0" stroke-width="0.9"/></svg>
        <span>012 345 6789</span>
      </div>
      <div class="contact__row">
        <svg class="contact__icon" viewBox="0 0 12 12"><circle cx="6" cy="6" r="5.3" fill="none" stroke="#1ea7e0" stroke-width="1"/><rect x="3.3" y="4" width="5.4" height="4" fill="none" stroke="#1ea7e0" stroke-width="0.9"/><path d="M3.3 4l2.7 2 2.7-2" fill="none" stroke="#1ea7e0" stroke-width="0.9"/></svg>
        <span>info@skyvoraq.com</span>
      </div>
    </div>
  </section>

  <section class="card card--back">
    <div class="brand">
      <div class="brand__mark"></div>
      <div class="brand__name">SKYVORAQ</div>
    </div>
    <div class="website">www.skyvoraq.com</div>
  </section>
</body>
</html>
```